Tallowbrook Paws Postboardly Ad

Need to incorporate the logo
Special postboardly discount - get $50 off any package (the main focus of the ad)
First walk free
link to website: www.tallowbrookpaws.com
tag: "is your dog a tallowbrookpaws?
Target Market(s)
The target audience is dog owners in Burnaby with a household income of 100,000 plus. People that can afford dogs but because they are working full-time or long hours are not able to.
Font styles to use
Sans Serif
Colors
acd036
Requirements
Must have
- Focus on the $50 off any package

```html
<!DOCTYPE html>
<html lang="en">
<head>
<meta charset="utf-8">
<title>Tallowbrook Paws – Postboardly Ad</title>
<link href="https://fonts.googleapis.com/css2?family=Jost:wght@300;400;600&family=Oswald:wght@500;600&display=swap" rel="stylesheet">
<style>
  :root {
    --backdrop: #8e8e8e;
    --grass: #8fa229;
    --grass-light: #a3b745;
    --slate: #46464f;
    --navy: #2d3d52;
    --paper: #ffffff;
    --glow: rgba(242, 250, 180, 0.85);
  }
  html, body {
    margin: 0;
    width: 1200px;
    height: 985px;
    overflow: hidden;
    background: var(--backdrop);
  }
  .ad-card {
    position: absolute;
    left: 40px;
    top: 106px;
    width: 1120px;
    height: 772px;
    background: var(--paper);
    overflow: hidden;
  }
  .ad-backdrop {
    position: absolute;
    left: 0;
    top: 0;
    width: 1120px;
    height: 677px;
  }
  .line {
    position: absolute;
    left: 0;
    width: 100%;
    text-align: center;
    margin: 0;
    white-space: nowrap;
  }
  .tagline-lead {
    top: 88px;
    font: 300 78px/1 "Jost", sans-serif;
    color: var(--navy);
    letter-spacing: 1px;
  }
  .tagline-name {
    top: 190px;
    font: 300 78px/1 "Jost", sans-serif;
    color: var(--navy);
  }
  .tagline-name strong { font-weight: 600; }
  .offer-kicker {
    top: 336px;
    font: 600 48px/1 "Oswald", sans-serif;
    color: var(--navy);
    text-shadow: 0 0 10px var(--glow), 0 0 4px var(--glow);
  }
  .offer-main {
    top: 378px;
    font: 600 80px/1.2 "Oswald", sans-serif;
    color: var(--navy);
    letter-spacing: 1px;
    text-shadow: 0 0 14px var(--glow), 0 0 5px var(--glow);
  }
  .offer-main .offer-amount {
    font-size: 120px;
    margin: 0 16px;
    vertical-align: -6px;
  }
  .walk-note {
    top: 580px;
    font: 400 17px/1 "Jost", sans-serif;
    color: var(--paper);
    letter-spacing: 0.5px;
  }
  .web-link {
    top: 606px;
    font: 400 32px/1 "Jost", sans-serif;
    color: var(--paper);
    letter-spacing: 1px;
  }
  .brand-bar {
    position: absolute;
    left: 0;
    top: 677px;
    width: 100%;
    height: 95px;
    display: flex;
    align-items: center;
    justify-content: center;
    gap: 18px;
  }
  .brand-dot {
    width: 54px;
    height: 54px;
    border-radius: 50%;
    background: var(--grass);
  }
  .brand-name {
    font: 400 40px/1 "Jost", sans-serif;
    color: var(--slate);
    letter-spacing: 1px;
  }
</style>
</head>
<body>
  <main class="ad-card">
    <svg class="ad-backdrop" viewBox="0 0 1120 677" role="img" aria-label="Green background with a light glow behind the offer">
      <defs>
        <radialGradient id="offer-glow" cx="560" cy="420" r="620" gradientUnits="userSpaceOnUse">
          <stop offset="0" stop-color="var(--grass-light)"/>
          <stop offset="1" stop-color="var(--grass)"/>
        </radialGradient>
      </defs>
      <rect width="1120" height="677" fill="url(#offer-glow)"/>
      <polygon points="372,0 744,0 562,40" fill="var(--slate)"/>
      <polygon points="0,643 562,513 1120,643 1120,677 0,677" fill="var(--slate)"/>
    </svg>

    <p class="line tagline-lead">IS YOUR DOG A</p>
    <p class="line tagline-name"><strong>TALLOWBROOKPAWS</strong> DOG?</p>

    <p class="line offer-kicker">SPECIAL POSTBOARDLY DISCOUNT</p>
    <p class="line offer-main">GET<span class="offer-amount">$50 OFF</span>ANY PACKAGE</p>

    <p class="line walk-note">FIRST WALK FREE TO OUR WEBSITE</p>
    <p class="line web-link">WWW.TALLOWBROOKPAWS.COM</p>

    <footer class="brand-bar">
      <span class="brand-dot"></span>
      <span class="brand-name">TALLOWBROOK PAWS</span>
    </footer>
  </main>
</body>
</html>
```